4' x 8' Construction Project Sign, think of a very large business card

We need project signs for our construction sites, the sign will be mounted along the road so cars driving by can quickly read. the sign should be able to be read as cars drive by doing highway speed.

Think like your making a large business card

I would like to include "NOW HIRING" Superintendents, Project Managers, Pipe Foremen, Pipe Layers, and Equipment Operators

Description of services we provide should include

Civil Construction Services
Land Clearing
Excavation
Underground Utilities
Environmental Maintenance

The 2 objectives is to market to future clients and to recruit new employees

The sign will be mounted on posts at the entrance of our construction projects
Updates

Low design quality

Target Market(s)

Construction and land developers

Industry/Entity Type

Construction Company

Other font styles liked:
• Hypatia Sans Pro lite

Colors

Designer to choose colors to be used in the design.

Requirements
Must have
• Clean and easy to read
• Civil Construction Services
• Land Clearing
• Excavation
• Underground Utilities
• Road Construction

```html
<!DOCTYPE html>
<html lang="en">
<head>
<meta charset="utf-8">
<title>Harlow Ridge Civil Construction – Project Sign</title>
<link rel="stylesheet" href="https://fonts.googleapis.com/css2?family=Mukta:wght@500;600;700&display=swap">
<style>
  :root {
    --brand-blue: #1f3d7c;
    --brand-grey: #6d6e71;
    --ink: #111111;
    --paper-top: #ffffff;
    --paper-bottom: #e4e4e4;
    --backdrop: #dcdcdc;
    --white: #ffffff;
  }
  html, body {
    margin: 0;
    padding: 0;
    width: 1200px;
    height: 1200px;
    overflow: hidden;
    background: var(--backdrop);
    font-family: "Mukta", sans-serif;
  }
  .project-sign {
    position: absolute;
    left: 50px;
    top: 325px;
    width: 1100px;
    height: 550px;
    background: linear-gradient(180deg, var(--paper-top) 0%, var(--paper-bottom) 100%);
    overflow: hidden;
  }
  .brand-square {
    position: absolute;
    left: 150px;
    top: 80px;
    width: 90px;
    height: 90px;
    background: var(--brand-blue);
  }
  .brand-divider {
    position: absolute;
    left: 297px;
    top: 32px;
    width: 2px;
    height: 190px;
    background: var(--brand-grey);
  }
  .brand-name {
    position: absolute;
    left: 323px;
    top: 48px;
    width: 660px;
    margin: 0;
    font-size: 72px;
    font-weight: 600;
    line-height: 1;
    color: var(--brand-blue);
    letter-spacing: 2px;
    white-space: nowrap;
  }
  .brand-tagline {
    position: absolute;
    left: 325px;
    top: 132px;
    width: 660px;
    margin: 0;
    font-size: 40px;
    font-weight: 600;
    line-height: 1;
    color: var(--brand-grey);
    letter-spacing: 16px;
    white-space: nowrap;
  }
  .hiring-banner {
    position: absolute;
    left: 81px;
    top: 265px;
    width: 538px;
    height: 83px;
    margin: 0;
    background: var(--brand-blue);
    color: var(--white);
    font-size: 72px;
    font-weight: 600;
    line-height: 83px;
    text-align: center;
    letter-spacing: 1px;
    white-space: nowrap;
    overflow: hidden;
  }
  .hiring-roles {
    position: absolute;
    left: 40px;
    top: 378px;
    width: 600px;
    margin: 0;
    padding: 0;
    list-style: none;
    text-align: center;
  }
  .role-row {
    display: block;
    height: 38px;
    font-size: 28px;
    font-weight: 600;
    line-height: 38px;
    color: var(--ink);
    white-space: nowrap;
  }
  .role {
    display: inline-block;
    margin: 0 9px;
  }
  .role::before {
    content: "";
    display: inline-block;
    width: 11px;
    height: 11px;
    margin-right: 6px;
    vertical-align: 4px;
    background: var(--brand-blue);
  }
  .column-divider {
    position: absolute;
    left: 670px;
    top: 256px;
    width: 6px;
    height: 244px;
  }
  .services-heading {
    position: absolute;
    left: 707px;
    top: 265px;
    width: 325px;
    height: 44px;
    margin: 0;
    background: var(--brand-blue);
    color: var(--white);
    font-size: 30px;
    font-weight: 500;
    line-height: 44px;
    text-align: center;
    white-space: nowrap;
  }
  .services-list {
    position: absolute;
    left: 690px;
    top: 313px;
    width: 360px;
    margin: 0;
    padding: 0;
    list-style: none;
    text-align: center;
  }
  .service {
    position: relative;
    height: 38.5px;
    font-size: 20px;
    font-weight: 600;
    line-height: 34px;
    color: var(--ink);
    white-space: nowrap;
  }
  .service + .service::before {
    content: "";
    position: absolute;
    left: 96px;
    top: -4px;
    width: 168px;
    height: 2px;
    border-radius: 50%;
    background: var(--brand-blue);
  }
  .sign-base-band {
    position: absolute;
    left: 0;
    bottom: 0;
    width: 1100px;
    height: 16px;
    background: var(--brand-blue);
  }
</style>
</head>
<body>
  <section class="project-sign">
    <span class="brand-square"></span>
    <span class="brand-divider"></span>
    <h1 class="brand-name">HARLOW RIDGE</h1>
    <p class="brand-tagline">CIVIL CONSTRUCTION</p>

    <h2 class="hiring-banner">NOW HIRING</h2>
    <ul class="hiring-roles">
      <li class="role-row"><span class="role">SUPERINTENDENTS</span><span class="role">PROJECT MANAGERS</span></li>
      <li class="role-row"><span class="role">PIPE FOREMEN</span><span class="role">PIPE LAYERS</span></li>
      <li class="role-row"><span class="role">EQUIPMENT OPERATORS</span></li>
    </ul>

    <svg class="column-divider" viewBox="0 0 6 244" aria-hidden="true">
      <g fill="#1f3d7c">
        <circle cx="3" cy="3" r="2.4"/><circle cx="3" cy="19" r="2.4"/><circle cx="3" cy="35" r="2.4"/>
        <circle cx="3" cy="51" r="2.4"/><circle cx="3" cy="67" r="2.4"/><circle cx="3" cy="83" r="2.4"/>
        <circle cx="3" cy="99" r="2.4"/><circle cx="3" cy="115" r="2.4"/><circle cx="3" cy="131" r="2.4"/>
        <circle cx="3" cy="147" r="2.4"/><circle cx="3" cy="163" r="2.4"/><circle cx="3" cy="179" r="2.4"/>
        <circle cx="3" cy="195" r="2.4"/><circle cx="3" cy="211" r="2.4"/><circle cx="3" cy="227" r="2.4"/>
        <circle cx="3" cy="241" r="2.4"/>
      </g>
    </svg>

    <h2 class="services-heading">Services We Provide</h2>
    <ul class="services-list">
      <li class="service">CIVIL CONSTRUCTION SERVICES</li>
      <li class="service">LAND CLEARING</li>
      <li class="service">EXCAVATION</li>
      <li class="service">UNDERGROUND UTILITIES</li>
      <li class="service">ENVIRONMENTAL MAINTENANCE</li>
    </ul>

    <span class="sign-base-band"></span>
  </section>
</body>
</html>
```